K&T Fixit and Rebuild general contracting business card design

I already have a logo that I want to use and I need a card that uses that logo and color scheme on the front with the address phone numbers and email and on the back a place for technicians to write in their name and phone number when they hand it out. It will need the License number of License #KTFXTRB318QN.
It should say General Contractor under the company name. The address is
4417 NE 3rd Ave, Ste D246
Vancouver, WA 98612
www.kandtfixitandrebuild.example
office@kandtfixitandrebuild.example
360-555-0182 is the telephone number
360-555-0149 is the fax number

Target Market(s)

Homeowners needing remodel work or repairs in their home.

Industry/Entity Type

Construction

Contact Information for Business Card

Business name, address, phone number, license number, fax number, email, and website on the front and a place to fill in technician's name and number

Font styles to use
Serif

Requirements
Must have
• Business name, address, phone number, license number, fax number, email, and website on the front and a place to fill in technician's name and number
Nice to have
• I uploaded an example of a front that is good.
Should not have
• Froo froo or extra embellishments.

```html
<!DOCTYPE html>
<html lang="en">
<head>
<meta charset="utf-8">
<title>K&amp;T Fixit and Rebuild – Business Card</title>
<link rel="stylesheet" href="https://fonts.googleapis.com/css2?family=Michroma&family=Montserrat:wght@400;600;700&display=swap">
<style>
  :root {
    --page: #e4e4e4;
    --wood-light: #d08a52;
    --wood-mid: #c27a44;
    --wood-dark: #b0683a;
    --stripe: #d9a07a;
    --paper: #ffffff;
    --copper: #b8714a;
    --ink-light: #ffffff;
    --back-dark: #232323;
    --back-mid: #3e3e3e;
    --field: #f4f4f4;
  }
  * { box-sizing: border-box; margin: 0; padding: 0; }
  html, body { width: 1200px; height: 1200px; overflow: hidden; }
  body {
    background: var(--page);
    font-family: "Montserrat", sans-serif;
    position: relative;
  }
  .card {
    position: absolute;
    left: 180px;
    width: 840px;
    height: 480px;
    border-radius: 22px;
    overflow: hidden;
  }
  .card-front { top: 100px; }
  .card-back {
    top: 640px;
    background: linear-gradient(200deg, var(--back-mid) 0%, var(--back-dark) 60%);
  }
  .front-art { position: absolute; inset: 0; width: 100%; height: 100%; }
  .contact-block {
    position: absolute;
    left: 50px;
    top: 112px;
    color: var(--ink-light);
  }
  .person-name {
    font-family: "Michroma", sans-serif;
    font-size: 23px;
    letter-spacing: 0.5px;
    line-height: 1.2;
  }
  .person-role { font-size: 17px; margin-top: 2px; }
  .address { font-size: 17px; line-height: 23px; margin-top: 14px; }
  .contact-list { list-style: none; margin-top: 14px; font-size: 16.5px; line-height: 23px; }
  .contact-list li { display: flex; align-items: center; gap: 10px; }
  .contact-list svg { width: 15px; height: 15px; flex: none; fill: var(--ink-light); }
  .license { font-size: 17px; margin-top: 16px; }
  .brand-name {
    position: absolute;
    font-family: "Montserrat", sans-serif;
    font-weight: 700;
    color: var(--copper);
    text-align: center;
    line-height: 1.15;
  }
  .card-front .brand-name { left: 520px; width: 280px; top: 196px; font-size: 30px; }
  .card-back .brand-name { left: 60px; width: 310px; top: 200px; font-size: 32px; }
  .write-in { position: absolute; left: 384px; width: 392px; }
  .write-in-label {
    font-weight: 600;
    font-size: 17px;
    color: var(--copper);
    text-transform: uppercase;
    letter-spacing: 0.2px;
  }
  .write-in-field { height: 29px; background: var(--field); margin-top: 6px; margin-left: 2px; }
  .write-in-name { top: 170px; }
  .write-in-phone { top: 261px; }
</style>
</head>
<body>
  <section class="card card-front">
    <svg class="front-art" viewBox="0 0 800 457" preserveAspectRatio="none">
      <defs>
        <linearGradient id="woodTone" x1="0" y1="0" x2="1" y2="1">
          <stop offset="0" stop-color="var(--wood-light)"/>
          <stop offset="0.5" stop-color="var(--wood-mid)"/>
          <stop offset="1" stop-color="var(--wood-dark)"/>
        </linearGradient>
      </defs>
      <rect class="wood-panel" width="800" height="457" fill="url(#woodTone)" role="img" aria-label="Wood grain texture panel"/>
      <polygon class="divider-stripe" points="578,0 800,0 800,457 590,457 355,228" fill="var(--stripe)"/>
      <polygon class="divider-gap" points="584,0 800,0 800,457 596,457 364,228" fill="var(--paper)"/>
      <polygon class="paper-panel" points="598,0 800,0 800,457 606,457 375,228" fill="var(--paper)"/>
      <polygon class="inner-stripe" points="590,0 598,0 375,228 606,457 598,457 367,228" fill="var(--stripe)"/>
    </svg>

    <div class="contact-block">
      <h1 class="person-name">DANIEL BROOKS</h1>
      <p class="person-role">General Contractor</p>
      <p class="address">4417 NE 3rd Ave, Ste D246<br>Vancouver, WA 98612</p>
      <ul class="contact-list">
        <li>
          <svg viewBox="0 0 16 16"><path d="M3.5 1 6 1.5 7 5 5.3 6.3c.9 1.8 2.5 3.4 4.4 4.4L11 9l3.5 1 .5 2.5-2 2C7 14 2 9 1.5 3z"/></svg>
          360-555-0182
        </li>
        <li>
          <svg viewBox="0 0 16 16"><rect x="4" y="1" width="8" height="5"/><rect x="1" y="7" width="14" height="6" rx="1"/><rect x="4" y="11" width="8" height="4" fill="var(--wood-mid)"/></svg>
          360-555-0149
        </li>
        <li>
          <svg viewBox="0 0 16 16"><path d="M1 3h14v10H1z M1 3l7 6 7-6" stroke="var(--wood-mid)" stroke-width="1.2"/></svg>
          office@kandtfixitandrebuild.example
        </li>
        <li>
          <svg viewBox="0 0 16 16"><circle cx="8" cy="8" r="7"/><path d="M1 8h14M8 1c-3 3-3 11 0 14M8 1c3 3 3 11 0 14" stroke="var(--wood-mid)" stroke-width="1" fill="none"/></svg>
          kandtfixitandrebuild.example
        </li>
      </ul>
      <p class="license">Lic No: #KTFXTRB318QN.</p>
    </div>

    <p class="brand-name">K&amp;T Fixit<br>and Rebuild</p>
  </section>

  <section class="card card-back">
    <p class="brand-name">K&amp;T Fixit<br>and Rebuild</p>
    <div class="write-in write-in-name">
      <p class="write-in-label">Technician's Name</p>
      <div class="write-in-field"></div>
    </div>
    <div class="write-in write-in-phone">
      <p class="write-in-label">Phone Number</p>
      <div class="write-in-field"></div>
    </div>
  </section>
</body>
</html>
```